Pelican Media Website Design

Home page & interior page design.

Target Market(s)

Small businesses or at home businesses. Budget $1,000 - $3,000.

Industry/Entity Type

Media

Number of Pages Required

2 pages

Requirements
Must have
• Home page must consist of:
- Logo in top left
- Bannerimagery showcasing design examples (to be provided)
- 4 main modules, directing users to the 4 main product areas:
1. Templated brochure websites
2. Custom designed brochure websites
3. eCommerce websites
4. SEO

Area for text to be inserted (around 200 words) of introductory text

- Use of correct colour pallette based on logo provided
Nice to have
• Custom designed icons for the 4 main product areas.
Should not have
• Unstructured, cluttered layout

```html
<!DOCTYPE html>
<html lang="en">
<head>
<meta charset="utf-8">
<title>Pelican Media</title>
<link href="https://fonts.googleapis.com/css2?family=Arimo:wght@400;700&family=Tinos:ital,wght@0,400;1,400;1,700&display=swap" rel="stylesheet">
<style>
:root{
  --gray-top:#8c8c8c;
  --gray-bottom:#6a6a6a;
  --amber:#eca100;
  --orange:#ec8404;
  --vermilion:#e04a1c;
  --crimson:#d2001f;
  --ink:#444;
  --panel:#5d5d5d;
  --link:#f7a600;
  --white:#fff;
}
*{box-sizing:border-box;margin:0;padding:0}
html,body{width:1151px;height:1200px;overflow:hidden;background:var(--white);font-family:"Arimo",Arial,sans-serif}
.page{position:relative;width:1151px;height:1200px}
.header-band{position:absolute;left:0;top:0;width:1151px;height:189px;background:linear-gradient(var(--gray-top),var(--gray-bottom));border-bottom:2px solid #555}
.brand{position:absolute;left:144px;top:20px;width:432px;height:142px;background:linear-gradient(#fff,#e9e9e9);border:2px solid #f3b800;border-bottom:none;border-radius:8px 8px 0 0;display:flex;align-items:center;justify-content:center}
.brand-name{font-family:"Arimo",Arial,sans-serif;font-weight:700;font-size:50px;color:var(--orange);letter-spacing:-1px}
.nav-tabs{position:absolute;left:802px;top:133px;width:192px;height:30px;background:linear-gradient(#fff,#ddd);border-radius:6px 6px 0 0;display:flex;align-items:center;justify-content:center;gap:14px;font-size:16px;color:#777}
.nav-tabs .sep{width:1px;height:18px;background:#aaa}
.modules{position:absolute;left:145px;top:161px;width:862px;height:273px;display:flex;border-radius:0 6px 6px 6px;overflow:hidden}
.module{position:relative;flex:1;overflow:hidden}
.module:nth-child(1){background:var(--amber)}
.module:nth-child(2){background:var(--orange)}
.module:nth-child(3){background:var(--vermilion)}
.module:nth-child(4){background:var(--crimson)}
.module-art{position:absolute;right:0;bottom:0;width:130px;height:190px;background:linear-gradient(160deg,rgba(255,255,255,.55),rgba(255,255,255,.25));border-top-left-radius:6px}
.module-label{position:absolute;left:12px;bottom:12px;writing-mode:vertical-rl;transform:rotate(180deg);font-family:"Tinos",serif;color:#3a2400;display:flex;gap:2px}
.module-label .title{font-style:italic;font-size:30px;line-height:32px}
.module-label .sub{font-size:19px;line-height:22px;opacity:.7}
.intro{position:absolute;left:144px;top:451px;width:628px;height:453px;border:1px solid #ddd;border-radius:5px;box-shadow:0 1px 3px rgba(0,0,0,.15);padding:18px 17px 0 17px}
.intro h1{font-family:"Tinos",serif;font-style:italic;font-size:44px;font-weight:400;color:var(--orange);line-height:46px;margin-left:-2px}
.intro h1 b{color:#e0401a;font-weight:700}
.intro p{font-size:12.4px;line-height:17.1px;color:var(--ink);margin-top:17px;width:596px}
.intro p + p{margin-top:17px}
.btn-more{position:absolute;display:inline-block;background:linear-gradient(#f8a820,#e47c00);color:#fff;font-weight:700;font-size:11px;padding:3px 6px;border-radius:4px}
.intro .btn-more{left:14px;bottom:17px}
.showcase{position:absolute;left:790px;top:451px;width:217px;height:453px;background:var(--panel);border:2px solid #888;border-radius:4px}
.showcase h2{font-family:"Tinos",serif;font-style:italic;font-weight:400;font-size:36px;color:#eee;height:52px;line-height:50px;padding-left:10px;border-bottom:2px solid #888;background:linear-gradient(#6c6c6c,#5a5a5a)}
.work{margin:0 11px;padding:9px 0 12px;border-bottom:1px solid #888}
.work a{display:block;font-size:12px;color:var(--link);text-decoration:none;margin-bottom:8px}
.work .shot{height:74px;border:2px solid #ddd}
.shot-a{background:linear-gradient(90deg,#eee 30%,#d9d9d9)}
.shot-b{background:linear-gradient(#1a9ad0,#5cb6df 70%,#333 92%)}
.shot-c{background:linear-gradient(#fff 25%,#4a8ed0 26%,#6aaae0)}
.showcase .btn-more{left:11px;bottom:10px}
.footer-bar{position:absolute;left:144px;top:977px;width:863px;height:73px;border:3px solid #fff;border-radius:10px;background:linear-gradient(#f6c418,#f0a10a 40%,#ec7f02);box-shadow:0 0 4px rgba(230,120,0,.6);display:flex;align-items:flex-end;justify-content:center;padding-bottom:13px;font-size:13px;color:#fde3b0;gap:12px}
.wordmark{position:absolute;left:432px;top:1058px;width:288px;text-align:center;font-family:"Tinos",serif;font-style:italic;font-size:28px;color:#aaa;border-bottom:2px solid #e04a1c;padding-bottom:4px}
.copyright{position:absolute;left:432px;top:1100px;width:288px;text-align:center;font-size:10px;color:var(--orange)}
</style>
</head>
<body>
<div class="page">
  <div class="header-band"></div>
  <div class="brand"><span class="brand-name">Pelican Media</span></div>
  <nav class="nav-tabs"><span>About</span><span class="sep"></span><span>Contact us</span></nav>

  <section class="modules">
    <div class="module">
      <div class="module-art" role="img" aria-label="Icon of stacked templated web pages"></div>
      <div class="module-label"><span class="title">Templated</span><span class="sub">brochure websites</span></div>
    </div>
    <div class="module">
      <div class="module-art" role="img" aria-label="Icon of custom designed pages with a star"></div>
      <div class="module-label"><span class="title">Custom designed</span><span class="sub">brochure websites</span></div>
    </div>
    <div class="module">
      <div class="module-art" role="img" aria-label="Icon of a shopping basket"></div>
      <div class="module-label"><span class="title">eCommerce</span><span class="sub">websites</span></div>
    </div>
    <div class="module">
      <div class="module-art" role="img" aria-label="Icon of a rising bar chart"></div>
      <div class="module-label"><span class="title">SEO</span><span class="sub">services</span></div>
    </div>
  </section>

  <main class="intro">
    <h1><b>What</b> we do</h1>
    <p>Lorem ipsum dolor sit amet, consectetur adipiscing elit. Aliquam non felis lectus, eget porta erat. Nullam ac leo eros, at sodales leo. Lorem ipsum dolor sit amet, consectetur adipiscing elit. Vestibulum ante ipsum primis in faucibus orci luctus et ultrices posuere cubilia Curae; Suspendisse potenti. Duis faucibus semper diam eu vestibulum. Class aptent taciti sociosqu ad litora torquent per conubia nostra, per inceptos himenaeos. Praesent et arcu dolor. Nunc suscipit fringilla quam vel elementum. Vivamus elit felis, malesuada ut commodo quis, accumsan ac sem. Etiam venenatis molestie nulla sed congue. Aenean vel enim ultricies purus blandit elementum. Etiam non scelerisque elit. Nunc mattis hendrerit enim. Ut accumsan sem nec arcu dapibus tempor.</p>
    <p>Pellentesque hendrerit enim et leo tincidunt non ornare odio ultricies. Etiam vestibulum dapibus ligula id pretium. Maecenas semper diam non metus sagittis laoreet. Nulla sit amet tortor nec odio venenatis vehicula. Fusce consectetur porta urna, molestie porta felis elementum vitae. Cum sociis natoque penatibus et magnis dis parturient montes, nascetur ridiculus mus. In quis leo nibh. Aenean nec enim sit amet mauris faucibus rutrum. Fusce nec tortor quis sapien euismod sodales ut sit amet elit. Cras nisi metus, ornare quis condimentum ac, tempor sed eros. Ut vitae urna vitae lorem scelerisque pharetra. Aenean commodo iaculis enim nec aliquet. Proin rutrum odio vel ligula molestie quis consectetur turpis auctor. Mauris ante nunc, aliquam tincidunt rutrum ac, porta nec turpis. Vestibulum ante ipsum primis in faucibus orci luctus et ultrices posuere cubilia Curae; Donec gravida viverra velit, in semper nisi.</p>
    <span class="btn-more">See more »</span>
  </main>

  <aside class="showcase">
    <h2>Showcase</h2>
    <div class="work"><a>www.velvetgown.com.au</a><div class="shot shot-a" role="img" aria-label="Screenshot of a fashion store website"></div></div>
    <div class="work"><a>www.fitcoach.com.au</a><div class="shot shot-b" role="img" aria-label="Screenshot of a fitness academy website"></div></div>
    <div class="work"><a>www.datapoint.com.au</a><div class="shot shot-c" role="img" aria-label="Screenshot of a business information services website"></div></div>
    <span class="btn-more">See more »</span>
  </aside>

  <footer class="footer-bar">
    <span>Templated brochure websites</span><span>|</span><span>Custom designed brochure websites</span><span>|</span><span>eCommerce websites</span><span>|</span><span>SEO</span><span>|</span><span>About</span><span>|</span><span>Contact Us</span>
  </footer>
  <div class="wordmark">www.pelicanmedia.com</div>
  <div class="copyright">Copyright © 2009 Pelican Media</div>
</div>
</body>
</html>
```